Fresh Start Body Quest 2017 Poster

We are having a Fresh Start, Body Quest for 2017 at our fitness studio. We need a poster design using the template attached as a reference (Only reference). I have also included our Drovelux logo to put on the poster. Please DO NOT use the graphics in the flyer as we are expecting something much much better :-)
MUST HAVES:
- Size needed 11x17 with bleeding for printing
- .PSD File Format WITH LAYERS (CS3 Compatible)*** A MUST
- Use Drovelux Bootcamps Logo
- Use Information in the attached word doc

```html
<!DOCTYPE html>
<html lang="en">
<head>
<meta charset="utf-8">
<title>Fresh Start, Body Quest – Drovelux Bootcamps</title>
<link rel="stylesheet" href="https://fonts.googleapis.com/css2?family=Rubik+Dirt&family=Teko:wght@400;500;600&family=Roboto+Slab:wght@400;500;700;800&display=swap">
<style>
  :root {
    --teal: #13b0b8;
    --teal-deep: #0e8a91;
    --black: #0d0d0d;
    --charcoal: #262626;
    --charcoal-soft: #333333;
    --orange: #f58220;
    --lime: #e6e41f;
    --yellow: #f2ec2e;
    --grey: #a3a3a3;
    --grey-text: #b5b5b5;
    --white: #ffffff;
  }
  * { box-sizing: border-box; }
  html, body { margin: 0; padding: 0; overflow: hidden; background: var(--charcoal); }
  .poster {
    position: relative;
    width: 777px;
    height: 1200px;
    overflow: hidden;
    background: radial-gradient(ellipse at 50% 60%, var(--charcoal-soft), #1a1a1a 75%);
    font-family: "Roboto Slab", Georgia, serif;
    color: var(--black);
  }

  /* header */
  .header {
    position: absolute; left: 0; top: 0;
    width: 777px; height: 330px;
    background: linear-gradient(160deg, var(--teal) 0%, var(--teal) 60%, var(--teal-deep) 100%);
    clip-path: polygon(0 0, 100% 0, 100% 82%, 0 100%);
    padding: 46px 40px 0;
  }
  .title {
    margin: 0;
    font-family: "Rubik Dirt", Impact, sans-serif;
    font-weight: 400;
    font-size: 84px;
    line-height: 96px;
    white-space: nowrap;
  }
  .title__line { display: block; }
  .title__line--dark { color: var(--black); }
  .title__line--bright { color: var(--yellow); }
  .title-rule {
    width: 150px; height: 8px;
    margin-top: 18px;
    background: var(--black);
  }

  /* tagline */
  .tagline {
    position: absolute; left: 40px; top: 350px;
    width: 697px;
    margin: 0;
    padding-left: 22px;
    border-left: 8px solid var(--yellow);
    font-weight: 800;
    font-size: 27px;
    line-height: 40px;
    color: var(--grey-text);
  }

  /* schedule */
  .schedule {
    position: absolute; left: 40px; top: 470px;
    width: 380px; height: 470px;
    background: var(--orange);
    padding: 26px 26px 0;
  }
  .schedule__item {
    padding: 14px 0;
    border-bottom: 2px solid rgba(0,0,0,0.18);
  }
  .schedule__item:first-child { padding-top: 0; }
  .schedule__item:last-child { border-bottom: 0; }
  .schedule__label {
    display: block;
    font-weight: 800;
    font-size: 21px;
    line-height: 28px;
  }
  .schedule__detail {
    display: block;
    font-weight: 500;
    font-size: 21px;
    line-height: 30px;
  }
  .schedule__item--finale .schedule__label { font-size: 20px; }
  sup { font-size: 12px; line-height: 0; }

  /* prize */
  .prize {
    position: absolute; left: 440px; top: 470px;
    width: 297px; height: 170px;
    background: var(--lime);
    text-align: center;
    padding-top: 22px;
    font-family: "Teko", "Arial Narrow", sans-serif;
  }
  .prize__amount { display: block; font-weight: 500; font-size: 74px; line-height: 70px; }
  .prize__note { display: block; font-weight: 400; font-size: 38px; line-height: 44px; }

  /* program */
  .program {
    position: absolute; left: 440px; top: 660px;
    width: 297px; height: 280px;
    background: var(--grey);
    text-align: center;
    padding-top: 26px;
  }
  .program__heading {
    display: block;
    font-family: "Teko", "Arial Narrow", sans-serif;
    font-weight: 500;
    font-size: 56px;
    line-height: 52px;
  }
  .program__services {
    display: block;
    margin-top: 8px;
    font-weight: 500;
    font-size: 22px;
    line-height: 30px;
  }
  .program__offer {
    display: block;
    margin-top: 14px;
    font-weight: 800;
    font-size: 24px;
    line-height: 30px;
    color: var(--yellow);
  }
  .program__price { font-size: 52px; line-height: 56px; }

  /* info */
  .info {
    position: absolute; left: 0; top: 966px;
    width: 777px; height: 96px;
    background: var(--teal);
    text-align: center;
    padding-top: 12px;
    color: var(--white);
  }
  .info__lead {
    display: block;
    font-family: "Teko", "Arial Narrow", sans-serif;
    font-weight: 400;
    font-size: 40px;
    line-height: 40px;
  }
  .info__url { display: block; font-weight: 800; font-size: 25px; line-height: 32px; }

  /* brand */
  .brand {
    position: absolute; left: 203px; top: 1090px;
    width: 371px; height: 80px;
    background: var(--white);
    display: flex; align-items: center; justify-content: center; gap: 14px;
  }
  .brand__square { width: 22px; height: 22px; background: var(--teal); }
  .brand__name { font-weight: 800; font-size: 28px; color: var(--charcoal); letter-spacing: 1px; }
</style>
</head>
<body>
<main class="poster">
  <header class="header">
    <h1 class="title">
      <span class="title__line title__line--dark">FRESH START,</span>
      <span class="title__line title__line--bright">BODY QUEST</span>
    </h1>
    <div class="title-rule"></div>
  </header>

  <p class="tagline">In Just 6 Weeks, Transform Your Body<br>And Get In The Best Shape Of Your Life!</p>

  <section class="schedule">
    <div class="schedule__item">
      <span class="schedule__label">KICK OFF MEETING:</span>
      <span class="schedule__detail">Thursday, Jan 12<sup>th</sup></span>
      <span class="schedule__detail">7:30pm</span>
    </div>
    <div class="schedule__item">
      <span class="schedule__label">START DATE:</span>
      <span class="schedule__detail">Tuesday, January 17<sup>th</sup></span>
    </div>
    <div class="schedule__item">
      <span class="schedule__label">END DATE:</span>
      <span class="schedule__detail">Saturday, February 25<sup>th</sup></span>
    </div>
    <div class="schedule__item schedule__item--finale">
      <span class="schedule__label">FINALE PARTY ON MARCH 2<sup>nd</sup></span>
    </div>
  </section>

  <section class="prize">
    <span class="prize__amount">$500 CASH</span>
    <span class="prize__note">PRIZE FOR WINNER</span>
  </section>

  <section class="program">
    <span class="program__heading">6 WEEKS OF</span>
    <span class="program__services">Training, Nutrition,<br>&amp; Coaching</span>
    <span class="program__offer">Starting at just<br><span class="program__price">$99!</span></span>
  </section>

  <section class="info">
    <span class="info__lead">FOR MORE INFO, VISIT</span>
    <span class="info__url">www.droveluxbootcamps.com</span>
  </section>

  <footer class="brand">
    <span class="brand__square"></span>
    <span class="brand__name">DROVELUX BOOTCAMPS</span>
  </footer>
</main>
</body>
</html>
```